Brannigan Ashcroft LLC. custom built/handcrafted

I am recent small business owner looking to sell my art(drawings) and woodworking projects from my home. I have a very rough draft of a simple card design created on a simple digital program. I was hoping for a fancier lettering on the initial letters (BA). More of a calligraphy style. Also, the yellow border around the logo I would like to be a gold foil look. For it to be shiny or reflective look and to keep the other letters black with a consistent font on the card and the card white.

Target Market(s)

Local and neighboring cities

Industry/Entity Type

Art (drawing)/Woodworking

Contact Information for Business Card

My email tpashcroft@mailvane.net, phone number 949-517-3068. In the files provided it has a yellow border around the logo and I was looking to make that a gold foil.

Font styles to use
Serif
Decorative
Script

Requirements
Nice to have
• symbols for having a Pagebook and Picturely

```html
<!DOCTYPE html>
<html lang="en">
<head>
<meta charset="utf-8">
<title>Brannigan Ashcroft LLC. – Business Card</title>
<link rel="stylesheet" href="https://fonts.googleapis.com/css2?family=Cormorant+Garamond:wght@500;600&family=Poppins:wght@400;500;700&display=swap">
<style>
  :root{
    --page:#ffffff;
    --card-white:#ffffff;
    --gold:#f0d08e;
    --gold-light:#fff2b8;
    --wood-top:#efd5a0;
    --wood-bottom:#e9cb92;
    --ink:#111111;
    --ghost:#e6e6e6;
  }
  *{box-sizing:border-box;margin:0;padding:0}
  html,body{width:1200px;height:2790px;overflow:hidden;background:var(--page)}
  .sheet{position:relative;width:1200px;height:2790px}
  .card{position:absolute;left:137px;width:926px;height:527px;box-shadow:0 8px 16px rgba(0,0,0,.28);overflow:hidden}
  .card--front{top:826px;background:var(--card-white)}
  .card--back{top:1437px;background:linear-gradient(180deg,var(--wood-top),var(--wood-bottom))}

  .front-border{position:absolute;inset:18px;border:5px solid var(--gold)}
  .ghost-name{position:absolute;left:30px;top:40px;width:500px;font-family:"Cormorant Garamond",serif;font-weight:600;font-size:78px;line-height:.95;color:var(--ghost);letter-spacing:2px;text-transform:uppercase}

  .logo-frame{position:absolute;border:2px solid var(--gold);display:flex;align-items:center;justify-content:center;text-align:center}
  .logo-name{font-family:"Cormorant Garamond",serif;font-weight:600;color:var(--ink);text-transform:uppercase;letter-spacing:1.5px;line-height:1.15}
  .tagline{position:absolute;font-family:"Cormorant Garamond",serif;font-weight:600;color:var(--ink);text-transform:uppercase;text-align:center;letter-spacing:.5px}

  .front-logo{left:558px;top:90px;width:228px;height:127px}
  .front-logo .logo-name{font-size:22px}
  .front-tagline{left:540px;top:228px;width:264px;font-size:11px}

  .owner{position:absolute;left:70px;top:282px;font-family:"Poppins",sans-serif;font-weight:700;font-size:20px;line-height:23px;color:var(--ink);text-transform:uppercase}
  .rule{position:absolute;left:70px;top:366px;width:770px;height:2px;background:var(--gold)}
  .contact{position:absolute;left:70px;top:397px;list-style:none;font-family:"Poppins",sans-serif;font-weight:500;font-size:18px;line-height:28px;color:var(--ink)}
  .contact li{display:flex;align-items:center;gap:12px}
  .contact svg{width:20px;height:20px;flex:none}
  .social{position:absolute;left:660px;top:429px;font-family:"Poppins",sans-serif;font-weight:500;font-size:13px;color:#d9b467;letter-spacing:.3px}

  .back-frame{left:260px;top:139px;width:404px;height:224px;border:3px solid var(--gold-light)}
  .back-frame .logo-name{font-size:38px}
  .back-tagline{left:213px;top:380px;width:500px;font-size:17px}
</style>
</head>
<body>
<main class="sheet">
  <section class="card card--front" aria-label="Business card front">
    <div class="front-border"></div>
    <div class="ghost-name" aria-hidden="true">Brannigan Ashcroft</div>
    <div class="logo-frame front-logo"><span class="logo-name">Brannigan<br>Ashcroft</span></div>
    <p class="tagline front-tagline">Custom Built · Handcrafted</p>
    <p class="owner">Owner<br>Tobias P. Ashcroft</p>
    <div class="rule"></div>
    <ul class="contact">
      <li><svg viewBox="0 0 24 24" aria-hidden="true"><path fill="#e8c27a" d="M6.6 10.8a15 15 0 0 0 6.6 6.6l2.2-2.2c.3-.3.7-.4 1-.2 1.1.4 2.3.6 3.6.6.6 0 1 .4 1 1V20c0 .6-.4 1-1 1A17 17 0 0 1 3 4c0-.6.4-1 1-1h3.5c.6 0 1 .4 1 1 0 1.3.2 2.5.6 3.6.1.3 0 .7-.2 1z"/></svg>949-517-3068</li>
      <li><svg viewBox="0 0 24 24" aria-hidden="true"><rect x="2" y="5" width="20" height="14" rx="1" fill="#e8c27a"/><path d="M2.5 5.5 12 13l9.5-7.5" fill="none" stroke="#fff" stroke-width="1.5"/></svg>tpashcroft@mailvane.net</li>
    </ul>
    <p class="social">Pagebook · Picturely</p>
  </section>

  <section class="card card--back" aria-label="Business card back">
    <div class="logo-frame back-frame"><span class="logo-name">Brannigan<br>Ashcroft</span></div>
    <p class="tagline back-tagline">Custom Built · Handcrafted</p>
  </section>
</main>
</body>
</html>
```